Hollowmere Farm Promotional Leaflet

The team at Hollowmere Farm can help with every aspect of managing and enhancing your home from housekeeping and professional cleaning, laundry and ironing to providing chic and contemporary flower arrangements and even food for your pets!We take pride in providing high-end, consistent and reliable professional services bespoke to you. Whether you are a busy professional working long hours, a stay-at home parent or retired; having professional help in the home gives you time to spend on the things you enjoy.We are providing a very upmarket, highly professional service and need an A5 promotional leaflet to be designed. Please refer to www.hollowmerefarm-example.co.uk and see the section on 'Home Management'The leaflet should incorporate the Hollowmere Farm logo without the 'tipi', and any suitable photography images used on the home page of the website or the 'home management' section.

Target Market(s)

high-end, affluent owners of luxury homes

Industry/Entity Type

Farm

Contact Information for Business Card

The business card design needs to be suitable for use across all of Hollowmere Farm businesses, specifically:
Hollowmere Farm Home Management - otherwise known as Hollowmere Farm @ Home (this uses the typographical logo
Hollowmere Farm Weddings & Events - this uses the 'tipi' logo

Requirements
Must have
• Design in keeping with the look and feel of the logo and website design
• www.hollowmerefarm-example.co.uk

```html
<!DOCTYPE html>
<html lang="en">
<head>
<meta charset="utf-8">
<title>Hollowmere Farm – Home Management Leaflet</title>
<link rel="stylesheet" href="https://fonts.googleapis.com/css2?family=Open+Sans:wght@400;600;700&family=Playfair+Display:wght@700&display=swap">
<style>
  :root{
    --magenta:#d81b5c;
    --charcoal:#3a3a3c;
    --ink:#1f1f21;
    --white:#ffffff;
    --stage:#ececec;
    --body-top:#f6f6f6;
    --body-bottom:#d4d4d6;
    --photo-light:#e8cfd6;
    --photo-mid:#b88c9b;
    --photo-dark:#6e4a57;
  }
  *{box-sizing:border-box;margin:0;padding:0}
  html,body{width:1200px;height:1000px;overflow:hidden;background:var(--stage)}
  body{font-family:"Open Sans",Arial,sans-serif;color:var(--ink);position:relative}

  .leaflet{
    position:absolute;left:260px;top:19px;width:680px;height:962px;overflow:hidden;
    background:linear-gradient(180deg,var(--body-top) 40%,var(--body-bottom) 100%);
    box-shadow:0 4px 18px rgba(0,0,0,.18);
  }

  /* hero */
  .hero-photo{
    position:absolute;left:0;top:0;width:680px;height:400px;
    background:
      radial-gradient(ellipse at 50% 10%,rgba(255,240,240,.9),transparent 45%),
      radial-gradient(ellipse at 30% 75%,var(--photo-light),transparent 40%),
      radial-gradient(ellipse at 78% 75%,var(--photo-light),transparent 35%),
      linear-gradient(180deg,var(--photo-mid) 0%,#c9a2ad 45%,var(--photo-dark) 100%);
  }
  .hero-band{position:absolute;left:0;top:350px;width:680px;height:70px}
  .brand-pill{
    position:absolute;left:190px;top:38px;width:300px;height:82px;border-radius:41px;
    background:var(--charcoal);display:flex;align-items:center;justify-content:center;gap:12px;
  }
  .brand-pill .brand-mark{width:12px;height:12px;border-radius:50%;background:var(--magenta)}
  .brand-pill .brand-name{font-weight:600;font-size:26px;color:var(--magenta);letter-spacing:.5px}
  .hero-headline{
    position:absolute;left:60px;top:180px;width:560px;text-align:center;
    font-family:"Playfair Display",Georgia,serif;font-weight:700;font-size:33px;line-height:1.2;
    color:var(--white);text-shadow:0 2px 6px rgba(60,20,35,.45);
  }

  /* body */
  .intro{position:absolute;left:30px;top:424px;width:636px;font-weight:700;font-size:14px;line-height:1.4}
  .services{
    position:absolute;left:28px;top:474px;width:250px;height:228px;padding:30px 12px 0 16px;
    background:var(--magenta);clip-path:polygon(0 6%,100% 0,100% 100%,0 100%);
  }
  .tick-list{list-style:none;color:var(--white);font-size:12px;line-height:1.36}
  .tick-list li{padding-left:13px;position:relative}
  .tick-list li::before{content:"›";position:absolute;left:0;top:-1px}
  .kitchen-photo{
    position:absolute;left:305px;top:480px;width:380px;height:200px;
    border:4px solid var(--magenta);border-right:none;border-radius:100px 0 0 100px;
    background:linear-gradient(180deg,#e9e7e2 0%,#dcd8d0 42%,#2f3a36 44%,#23302c 100%);
  }
  .pride{position:absolute;left:30px;top:714px;width:636px;font-weight:700;font-size:14px;line-height:1.42}

  .contact{
    position:absolute;left:0;top:800px;width:392px;height:138px;padding:16px 30px 0 40px;
    background:var(--charcoal);border:4px solid var(--magenta);border-left:none;
    border-radius:0 69px 69px 0;color:var(--white);text-align:center;font-weight:600;
  }
  .contact .cta{font-size:14px;line-height:1.35;margin-bottom:10px}
  .contact .details{font-size:13px;line-height:1.4}

  .promise{
    position:absolute;left:430px;top:786px;width:230px;height:158px;padding:26px 10px 0 14px;
    background:var(--magenta);clip-path:polygon(0 12%,78% 0,100% 9%,100% 100%,0 100%);
  }
  .promise .tick-list{font-size:11.5px;line-height:1.3}
</style>
</head>
<body>
  <article class="leaflet">
    <header>
      <div class="hero-photo" role="img" aria-label="Photograph of an elegant living room with cream sofas and a chandelier, in soft pink tones"></div>
      <svg class="hero-band" viewBox="0 0 680 70" width="680" height="70" aria-hidden="true">
        <polygon points="0,50 170,12 680,12 680,70 0,70" fill="#f6f6f6"/>
        <polygon points="0,38 170,0 680,0 680,12 170,12 0,50" fill="#d81b5c"/>
        <polygon points="0,50 170,12 680,12 680,20 170,20 0,58" fill="#bdbdbf" opacity=".5"/>
      </svg>
      <div class="brand-pill">
        <span class="brand-mark"></span>
        <span class="brand-name">Hollowmere Farm</span>
      </div>
      <h1 class="hero-headline">We look after our clients’<br>homes and holiday<br>lets across South Somerset.</h1>
    </header>

    <p class="intro">The team @ Hollowmere Farm can help with every aspect ofmanaging and enhancing your home including:</p>

    <section class="services">
      <ul class="tick-list">
        <li>Regular housekeeping and professional cleaning</li>
        <li>Exit cleans</li>
        <li>One-off seasonal /party / building</li>
        <li>Laundry and ironing</li>
        <li>Chic and contemporary flower arrangements</li>
        <li>Car valeting</li>
        <li>Pet food delivery</li>
        <li>Dry cleaning</li>
      </ul>
    </section>

    <div class="kitchen-photo" role="img" aria-label="Photograph of a kitchen with dark green cabinets and a range cooker"></div>

    <p class="pride">We take pride in providing high-end, consistent and reliable professional services bespoke to you. Coming home to a beautiful environment and being able to relax and enjoy your time is something we all deserve.</p>

    <section class="contact">
      <p class="cta">Contact us to arrange a home visit and quotation:</p>
      <p class="details">E: info@hollowmerefarm-example.co.uk<br>T: 07700 900123<br>www.hollowmerefarm-example.co.uk</p>
    </section>

    <section class="promise">
      <ul class="tick-list">
        <li>Satisfaction guaranteed</li>
        <li>Professional staff you can trust and rely on</li>
        <li>Competitive rates</li>
        <li>CRB checked and referenced</li>
        <li>Member of the Home Services Trade Guild</li>
        <li>Fully Insured</li>
      </ul>
    </section>
  </article>
</body>
</html>
```